Singer Renvika needs a CD cover for a new song "Keep the morning glow"

Hi. My name is Renvika. I need a CD cover for my new song "Keep the morning glow"

I want the cover to be drawn with logos of my name and the song title only this time, so "Renvika" and "Keep the morning glow".

My song can be heard from my website: https://renvika.plomsite.example/

Those logos need to be artistic. And probably very colorful. And the logo "Renvika" is at the center. The logo "Keep morning glow" is around it. The background is also to be artistic and colorful.

jpg file is necessary.

I would appreciate that you would challenge this for me. Thanks.

Renvika

Target Market(s)

Music industry

Colors
fbee3e

Requirements
Must have
• The logos of my name and the song title only this time, so "Renvika" and "Keep the morning glow". The logos need to be original design.
Should not have
• Something not original product, dawn from someone's work

```html
<!DOCTYPE html>
<html lang="en">
<head>
<meta charset="UTF-8">
<title>Renvika – Keep the morning glow</title>
<link href="https://fonts.googleapis.com/css2?family=Oswald:wght@600;700&display=swap" rel="stylesheet">
<style>
  :root {
    --page: #ffffff;
    --glow-core: #fff6c8;
    --glow-gold: #fbee3e;
    --amber: #e9a53a;
    --ember: #c4502a;
    --violet: #9b4fd0;
    --lilac: #d9c2ee;
    --mint: #8fe0c8;
    --leaf: #2f9a3c;
    --teal: #2f7e8c;
    --ink-deep: #2b1d3a;
    --title-cream: #f1e6c4;
    --name-cream: #f6e7b0;
    --title-shadow: rgba(40, 25, 10, 0.55);
  }

  html, body {
    margin: 0;
    padding: 0;
    width: 1200px;
    height: 1200px;
    overflow: hidden;
    background: var(--page);
  }

  .cover {
    position: relative;
    width: 1200px;
    height: 1200px;
    overflow: hidden;
  }

  .cover__artwork {
    position: absolute;
    inset: 0;
    background:
      radial-gradient(circle at 50% 52%, var(--glow-core) 0%, rgba(251, 238, 62, 0.85) 14%, rgba(233, 165, 58, 0.55) 30%, rgba(233, 165, 58, 0) 48%),
      radial-gradient(circle at 52% 88%, rgba(196, 80, 42, 0.85) 0%, rgba(196, 80, 42, 0) 28%),
      radial-gradient(circle at 8% 78%, var(--leaf) 0%, rgba(47, 154, 60, 0) 40%),
      radial-gradient(circle at 92% 78%, var(--teal) 0%, rgba(47, 126, 140, 0) 38%),
      radial-gradient(circle at 30% 22%, var(--mint) 0%, rgba(143, 224, 200, 0) 26%),
      radial-gradient(circle at 50% 6%, var(--lilac) 0%, rgba(217, 194, 238, 0) 34%),
      radial-gradient(circle at 4% 20%, var(--violet) 0%, rgba(155, 79, 208, 0) 36%),
      radial-gradient(circle at 96% 16%, var(--violet) 0%, rgba(155, 79, 208, 0) 34%),
      radial-gradient(circle at 94% 60%, rgba(155, 79, 208, 0.8) 0%, rgba(155, 79, 208, 0) 30%),
      linear-gradient(180deg, #c9a6d8 0%, #b58a5a 45%, #3d6a3a 100%);
  }

  .cover__type {
    position: absolute;
    inset: 0;
    width: 1200px;
    height: 1200px;
  }

  .song-title {
    font-family: "Oswald", "Arial Narrow", sans-serif;
    font-weight: 700;
    font-size: 112px;
    letter-spacing: 6px;
    fill: var(--title-cream);
    text-transform: uppercase;
    filter: drop-shadow(0 4px 6px var(--title-shadow));
  }

  .artist-name {
    font-family: "Oswald", "Arial Narrow", sans-serif;
    font-weight: 700;
    font-size: 200px;
    letter-spacing: 4px;
    fill: var(--name-cream);
    text-transform: uppercase;
  }
</style>
</head>
<body>
  <main class="cover">
    <div class="cover__artwork" role="img" aria-label="Colourful collage of bursting fireworks and blossoming branches in purple, gold, green and teal radiating from a bright golden centre"></div>

    <svg class="cover__type" viewBox="0 0 1200 1200" xmlns="http://www.w3.org/2000/svg">
      <defs>
        <path id="title-arc" d="M 200 800 A 420 420 0 1 1 1000 800" fill="none"/>
      </defs>

      <text class="song-title">
        <textPath href="#title-arc" startOffset="50%" text-anchor="middle">Keep the morning glow</textPath>
      </text>

      <text class="artist-name" x="600" y="790" text-anchor="middle">Renvika</text>
    </svg>
  </main>
</body>
</html>
```